High Tech - Energy Efficiency Startup needs new look / feel for website

We are a high tech company focused on offering software, services and training courses aimed to create, design and optimize efficient Turbomachinery ( Think: Power Generation, Aerospace, Automotive, Oil & Gas, etc)

I am looking for somebody to design a new front page and 1 second level page. Then we will need to receive the photoshop files.

Here is what our website currently looks like:

www.velmorcode.com

here is our work in progress which is not quite there: ua.velmorcode.com << Look here for 1st and 2nd level, you will see they look different.

here is what we want it to look like in terms of look and feel and slickness...( our competitors)

www.Kordex.com
http://plimtaware.com

You can email questions to Gregory.Tallis@velmorcode.com
Updates

Hello All,

Several things I wanted to note / add:

1) For the Top Menu, we want to add another Item. "Industries" ( same way as Kordex has it)
2) If you find other features which you think we missed or would make sense...

Cheers,

Gregory

Reason: we have two top designs, but they are still not 100% perfect. I hope that somebody will step up and make something which will be truly amazing!

Reason: we still do not confident ending a project that's not 100% complete.

Industry/Entity Type

Training

Requirements
Must have
• If you look at our attempt to have a banner and then smaller sub squares.

The idea is that the banner moves, left to right and displayes larger version of the commercial in the little squares underneath

We need graphics for the banners. They should relate / correspond to the product / or services that is being displayed.

You can see our products and services on ua.velmorcode.com so the banners should correlate.

We are really going for minimal words, good graphics, slick and sexy web 2.0 100,00o person company look and feel.

The design / designer who wins, will be given an offer to work with us afterwords and design the rest of our online properties, as well as all of our marketing material.

Please with your application submit your hourly rate for contract work.

```html
<!DOCTYPE html>
<html lang="en">
<head>
<meta charset="utf-8">
<title>Velmorcode — Turbomachinery Mastered</title>
<link href="https://fonts.googleapis.com/css2?family=Arimo:wght@400;700&family=Source+Sans+3:wght@600;700;800&display=swap" rel="stylesheet">
<style>
:root{
  --brand-blue:#0b56a4;
  --deep-blue:#0a4f98;
  --title-blue:#0e5aa8;
  --red:#e3101e;
  --red-dark:#c20a14;
  --light-gray:#efefef;
  --rule:#cfcfcf;
  --text:#333;
  --white:#fff;
}
*{box-sizing:border-box;margin:0;padding:0}
html,body{width:995px;height:1200px;overflow:hidden;background:var(--white);font-family:Arimo,Arial,sans-serif;color:var(--text)}
.page{position:relative;width:995px;height:1200px}
.abs{position:absolute}

/* header */
.site-header{left:0;top:0;width:995px;height:116px;background:var(--brand-blue)}
.brand{left:28px;top:38px;display:flex;align-items:center;gap:10px;color:var(--white);font:800 34px/1 "Source Sans 3",sans-serif}
.brand-dot{width:18px;height:18px;border-radius:50%;background:var(--white)}
.lang-list{right:15px;top:6px;display:flex;gap:10px}
.lang{width:19px;height:13px;display:block}
.util-links{right:162px;top:45px;display:flex;gap:12px;color:var(--white);font:700 12px/1 Arimo,sans-serif;white-space:nowrap}
.search{left:846px;top:40px;width:134px;height:23px;background:var(--white);border:1px solid #ccc;border-radius:2px;font-size:11px;color:#999;padding:5px 8px}
.social{left:890px;top:85px;display:flex;gap:6px}
.social span{width:17px;height:17px;background:#3b7fcf;border:1px solid #8fb8e6;display:block}

/* nav */
.main-nav{left:20px;top:130px;width:960px;height:39px;display:flex;background:linear-gradient(#ee2230,var(--red-dark))}
.main-nav a{flex:1;text-align:center;color:var(--white);font:700 12.5px/39px Arimo,sans-serif;text-decoration:none;border-right:1px solid #f57a80}
.main-nav a:last-child{border-right:0}
.main-nav a.active{background:var(--red-dark)}

/* hero */
.hero{left:20px;top:169px;width:960px;height:369px;background:linear-gradient(115deg,#2c4f7d 0%,#5e86b6 30%,#27476f 50%,#8aa4c2 70%,#3d5f8a 100%)}
.hero-title{left:48px;top:366px;color:var(--white);font:800 63px/0.9 "Source Sans 3",sans-serif;letter-spacing:.3px}
.btn{display:inline-block;background:var(--red);color:var(--white);font:700 12px/27px Arimo,sans-serif;padding:0 12px;text-decoration:none}
.hero-btn{left:48px;top:489px}

/* dropdown */
.menu-l1{left:20px;top:170px;width:190px}
.menu-l1 li{list-style:none;height:25px;color:var(--white);font:700 12px/24px Arimo,sans-serif;padding:0 23px;display:flex;justify-content:space-between;border-bottom:1px solid rgba(255,255,255,.25)}
.menu-l1 .red{background:linear-gradient(#ec1d2a,var(--red-dark))}
.menu-l1 .blue{background:linear-gradient(#4b8fd6,#2f6fb8)}
.menu-l2{left:210px;top:195px;width:190px}
.menu-l2 li{list-style:none;height:26px;color:var(--white);font:400 12px/26px Arimo,sans-serif;padding-left:8px;background:linear-gradient(#4b8fd6,#2f6fb8);border-bottom:1px solid #6aa5e0}
.menu-l2 li.current{background:#c5dcf2;color:#1f4f86}

/* tiles */
.tile{top:552px;width:182px;height:163px}
.tile-img{height:124px}
.tile-label{height:39px;background:var(--deep-blue);color:var(--white);font:700 15px/39px "Source Sans 3",sans-serif;padding:0 8px;display:flex;justify-content:space-between}

/* content columns */
.col-title{color:var(--title-blue);font:700 19px/1 "Source Sans 3",sans-serif;padding-bottom:7px;border-bottom:1px solid var(--rule)}
.news{left:20px;top:737px;width:377px}
.news-item{display:flex;padding:17px 0 14px;border-bottom:1px solid var(--rule)}
.news-date{flex:none;width:81px;color:var(--title-blue);font:700 19px/1 "Source Sans 3",sans-serif}
.news-body h3{color:var(--title-blue);font:700 15px/1.1 "Source Sans 3",sans-serif;margin-bottom:6px}
.news-body p{font-size:12px;line-height:14px}
.read-more{display:block;margin-top:7px;color:var(--title-blue);font:700 12px/1 Arimo,sans-serif}
.see-all{margin-top:16px}
.stories{left:409px;top:737px;width:378px}
.story{display:flex;align-items:center;gap:20px;margin-top:18px}
.story + .story{margin-top:33px}
.client-mark{flex:none;width:110px;height:51px;border:1px solid #ccc;display:flex;align-items:center;justify-content:center;text-align:center;color:var(--title-blue);font:700 13px/1.1 "Source Sans 3",sans-serif}
.quote{color:var(--title-blue);font:700 15px/1.2 "Source Sans 3",sans-serif;letter-spacing:-.2px;white-space:nowrap}
.aside{left:797px;top:737px;width:183px}
.aside p{font-size:10.5px;line-height:13px;margin-top:5px}
.aside .col-title + p{margin-top:11px}
.aside p b{color:var(--title-blue)}
.aside .btn{margin-top:8px}
.aside .col-title.second{margin-top:24px}

/* footer */
.footer-contact{left:0;top:1068px;width:995px;height:94px;background:var(--light-gray);padding:23px 24px;color:#1f3d6b;font:700 12px/18px Arimo,sans-serif}
.footer-bar{left:0;top:1164px;width:995px;height:36px;background:var(--brand-blue);color:var(--white);font:400 12px/36px Arimo,sans-serif;padding:0 24px;display:flex;justify-content:space-between}
.footer-links span{margin:0 9px}
</style>
</head>
<body>
<div class="page">

  <header class="site-header abs"></header>
  <div class="brand abs"><span class="brand-dot"></span>Velmorcode</div>
  <div class="lang-list abs">
    <svg class="lang" viewBox="0 0 19 13"><rect width="19" height="13" fill="#1f3c8a"/><rect x="8" width="3" height="13" fill="#d22"/><rect y="5" width="19" height="3" fill="#d22"/></svg>
    <svg class="lang" viewBox="0 0 19 13"><rect width="19" height="4.4" fill="#111"/><rect y="4.4" width="19" height="4.3" fill="#d00"/><rect y="8.7" width="19" height="4.3" fill="#fc0"/></svg>
    <svg class="lang" viewBox="0 0 19 13"><rect width="6.4" height="13" fill="#1f3c9a"/><rect x="6.4" width="6.3" height="13" fill="#fff"/><rect x="12.7" width="6.3" height="13" fill="#e22"/></svg>
    <svg class="lang" viewBox="0 0 19 13"><rect width="19" height="13" fill="#e01010"/><rect x="3" y="3" width="3" height="3" fill="#fd0"/></svg>
    <svg class="lang" viewBox="0 0 19 13"><rect width="6.4" height="13" fill="#1a9a3a"/><rect x="6.4" width="6.3" height="13" fill="#fff"/><rect x="12.7" width="6.3" height="13" fill="#e22"/></svg>
    <svg class="lang" viewBox="0 0 19 13"><rect width="19" height="13" fill="#d11"/><rect y="3.3" width="19" height="6.4" fill="#fc0"/></svg>
    <svg class="lang" viewBox="0 0 19 13"><rect width="19" height="13" fill="#fff"/><circle cx="9.5" cy="6.5" r="3.5" fill="#d11"/></svg>
    <svg class="lang" viewBox="0 0 19 13"><rect width="19" height="13" fill="#e11"/><rect width="7.5" height="13" fill="#1a8a30"/></svg>
  </div>
  <nav class="util-links abs"><span>Sign In</span><span>|</span><span>+1-555-014-2290</span><span>|</span><span>info@velmorcode.com</span></nav>
  <div class="search abs">Search</div>
  <div class="social abs"><span></span><span></span><span></span><span></span></div>

  <nav class="main-nav abs">
    <a class="active">PRODUCTS &amp; SERVICES</a><a>INDUSTRIES</a><a>CORPORATE</a><a>CAREERS</a><a>CONTACT</a>
  </nav>

  <div class="hero abs" role="img" aria-label="Close-up of turbine blades in cool blue tones"></div>
  <ul class="menu-l1 abs">
    <li class="red"><span>Products</span><span>&gt;</span></li>
    <li class="blue"><span>Services</span><span>&gt;</span></li>
    <li class="red"><span>Education</span><span>&gt;</span></li>
  </ul>
  <ul class="menu-l2 abs">
    <li>Engineering Services Overview</li>
    <li>Preliminary Design Studies</li>
    <li class="current">Machine Analysis</li>
    <li>Project Definition</li>
  </ul>
  <h1 class="hero-title abs">TURBOMACHINERY<br>MASTERED.</h1>
  <a class="btn hero-btn abs">LEARN MORE &gt;</a>

  <div class="tile abs" style="left:20px">
    <div class="tile-img" role="img" aria-label="Colourful flow simulation of an impeller" style="background:linear-gradient(135deg,#1fd64a,#e6e63a 50%,#2aa0e0)"></div>
    <div class="tile-label"><span>SUBHEAD 1</span><span>&#8964;</span></div>
  </div>
  <div class="tile abs" style="left:215px">
    <div class="tile-img" role="img" aria-label="Front view of a jet engine fan" style="background:radial-gradient(circle,#2a2a2a 15%,#9a9a9a 45%,#e6e6e6 80%)"></div>
    <div class="tile-label"><span>SUBHEAD 2</span><span>&#8964;</span></div>
  </div>
  <div class="tile abs" style="left:409px">
    <div class="tile-img" role="img" aria-label="Thermal stress simulation of a turbine blade" style="background:linear-gradient(135deg,#bbb,#e33 40%,#fd3 55%,#2b8ae0 80%)"></div>
    <div class="tile-label"><span>SUBHEAD 2</span><span>&#8964;</span></div>
  </div>
  <div class="tile abs" style="left:604px">
    <div class="tile-img" role="img" aria-label="Steam turbine rotor blade rows" style="background:linear-gradient(160deg,#d7dde3,#6b6a66 45%,#9c7f5a 75%,#3e3a35)"></div>
    <div class="tile-label"><span>SUBHEAD 2</span><span>&#8964;</span></div>
  </div>
  <div class="tile abs" style="left:798px">
    <div class="tile-img" role="img" aria-label="Colour contour plot of a flow field" style="background:linear-gradient(180deg,#fff 5%,#2a6fe0 25%,#3de05a 45%,#e02020 60%,#f3e24a 75%,#2a6fe0)"></div>
    <div class="tile-label"><span>SUBHEAD 2</span><span>&#8964;</span></div>
  </div>

  <section class="news abs">
    <h2 class="col-title">NEWS</h2>
    <article class="news-item">
      <div class="news-date">04/02</div>
      <div class="news-body">
        <h3>BayTech Weekly features Velmorcode.</h3>
        <p>If you would like to request a quotation for engineering services or desire additional information, please...</p>
        <a class="read-more">Read More...</a>
      </div>
    </article>
    <article class="news-item">
      <div class="news-date">03/14</div>
      <div class="news-body">
        <h3>BayTech Weekly features Velmorcode.</h3>
        <p>If you would like to request a quotation for engineering services or desire additional information, please...</p>
        <a class="read-more">Read More...</a>
      </div>
    </article>
    <a class="btn see-all">SEE ALL &gt;</a>
  </section>

  <section class="stories abs">
    <h2 class="col-title">SUCCESS STORIES</h2>
    <div class="story"><div class="client-mark">Norvant</div><p class="quote">“ Some great client quote goes here”</p></div>
    <div class="story"><div class="client-mark">Quellan<br>Institute</div><p class="quote">“ Some great client quote goes here”</p></div>
  </section>

  <aside class="aside abs">
    <h2 class="col-title">REQUEST QUOTE</h2>
    <p>If you would like to request a quotation for engineering services or desire additional information, please click on the link and complete the form.</p>
    <p>Please review our <b>Privacy Policy</b></p>
    <a class="btn">REQUEST QUOTE &gt;</a>
    <h2 class="col-title second">SCHEDULE DEMO</h2>
    <p>If you would like to schedule a demo, please click on the link and complete the form.</p>
    <p>Please review our <b>Privacy Policy</b></p>
    <a class="btn">SCHEDULE DEMO &gt;</a>
  </aside>

  <footer class="footer-contact abs">
    +1-555-014-2290<br>info@velmorcode.com<br>42 Harbor Crest Drive Milbrook, MA 01990, USA.
  </footer>
  <div class="footer-bar abs">
    <span>Copyright © 2013 Velmorcode Inc. All rights reserved.</span>
    <span class="footer-links">Site Map<span>|</span>Terms and Conditions<span>|</span>Privacy</span>
  </div>

</div>
</body>
</html>
```